Pathways to Brightmoor Land Ventures

size of the ad - 8”x 10.75" plus 0.25" bleed
I would like an ad for a magazine that will stand out and make people want to read the ad.
The ad should not be crowded and people reading the ad will be able to read the text.
I would like it to be a creative and modern-day design.
the list of topics should not be the focus of the ad.
the text is attached.
If you decide to use people in the ad then please no ladies.
please note that leave over 1 inch for the bottom of the footer

```html
<!DOCTYPE html>
<html lang="en">
<head>
<meta charset="utf-8">
<title>Real Estate Course Ad</title>
<link href="https://fonts.googleapis.com/css2?family=Montserrat:wght@300;400;500;600;700;800&family=Roboto:wght@300;400&display=swap" rel="stylesheet">
<style>
  :root{
    --stage:#bababa;
    --paper:#ffffff;
    --navy:#0e426d;
    --sky:#7cc9f1;
    --slate:#3f5e88;
    --footer:#42bdec;
    --white:#ffffff;
  }
  *{margin:0;padding:0;box-sizing:border-box}
  html,body{width:1200px;height:1200px;overflow:hidden;background:var(--stage)}
  .page{position:absolute;left:210px;top:80px;width:780px;height:1040px;background:var(--paper);font-family:'Montserrat',sans-serif;color:var(--navy);overflow:hidden}
  .title{position:absolute;top:46px;left:0;width:100%;text-align:center;font-weight:800;font-size:57px;letter-spacing:0.5px;line-height:1}
  .skyline{position:absolute;left:330px;top:110px;width:450px;height:362px;background:radial-gradient(ellipse at 60% 55%,#4f86b8 0%,#7fa9cc 40%,#cddceb 70%,rgba(255,255,255,0) 85%)}
  .event-card{position:absolute;left:65px;top:148px;width:331px;height:314px;border-radius:0 70px 0 80px;overflow:hidden;text-align:center;color:var(--white)}
  .event-top{height:182px;background:var(--sky);padding-top:20px}
  .event-bottom{height:132px;background:var(--slate);padding-top:15px;font-family:'Roboto',sans-serif}
  .city{font-weight:600;font-size:32px;line-height:1}
  .rule{width:246px;margin:0 auto;border-top:1px dotted rgba(255,255,255,.8)}
  .rule.first{margin-top:12px}
  .sessions{font-weight:600;font-size:14.5px;padding:5px 0 6px}
  .start{font-weight:600;font-size:32px;line-height:1;margin-top:6px}
  .scholar{font-family:'Roboto',sans-serif;font-weight:300;font-size:16px;margin-top:12px}
  .early{font-family:'Montserrat',sans-serif;font-weight:600;font-size:18px}
  .early-copy{font-weight:400;font-size:15.5px;line-height:19px;margin-top:10px}
  .band{position:absolute;left:0;top:481px;width:100%;height:99px;background:var(--navy);color:var(--white);text-align:center}
  .band-head{font-weight:800;font-size:25.5px;margin-top:19px;letter-spacing:.4px}
  .band-tag{font-weight:400;font-size:19.5px;margin-top:8px;letter-spacing:.8px}
  .topics-head{position:absolute;top:606px;width:100%;text-align:center;font-size:27px;line-height:1}
  .topics-head b{font-weight:800}
  .topics-head span{font-weight:300}
  .topics{position:absolute;left:65px;top:658px;width:650px;display:grid;grid-template-columns:repeat(5,130px);row-gap:12px}
  .topic{text-align:center;height:128px}
  .topic svg{display:block;margin:0 auto}
  .topic p{font-weight:600;font-size:12.5px;line-height:16px;margin-top:12px}
  .footer{position:absolute;left:0;top:935px;width:100%;height:105px;background:var(--footer);border-top:1px dotted var(--navy)}
</style>
</head>
<body>
<div class="page">
  <h1 class="title">REAL ESTATE COURSE</h1>
  <div class="skyline" role="img" aria-label="Photograph of a cluster of modern glass skyscrapers"></div>
  <div class="event-card">
    <div class="event-top">
      <div class="city">Kellsbrook</div>
      <div class="rule first"></div>
      <div class="sessions">10 -Tuesday evenings sessions</div>
      <div class="rule"></div>
      <div class="start">Starting Feb.28</div>
      <div class="scholar">Limited Partial Scholarships</div>
    </div>
    <div class="event-bottom">
      <div class="early">Early Bird Special</div>
      <div class="early-copy">For those that started or would<br>like to go into real estate</div>
    </div>
  </div>
  <div class="band">
    <div class="band-head">PATHWAYS TO BRIGHTMOOR LAND VENTURES</div>
    <div class="band-tag">INVESTING IN KNOWLEDGE IS INVESTING IN OPPORTUNITIES.</div>
  </div>
  <div class="topics-head"><b>TOPICS:</b> <span>PARTIAL LISTING</span></div>
  <div class="topics">
    <div class="topic"><svg width="72" height="72" viewBox="0 0 72 72"><circle cx="36" cy="36" r="35" fill="none" stroke="#0e426d" stroke-width="1.5"/><circle cx="36" cy="36" r="32" fill="#0e426d"/><g fill="none" stroke="#fff" stroke-width="1.6"><circle cx="38" cy="30" r="9"/><path d="M38 25v5h4M33 20l5-4 5 4"/><path d="M18 44h8l8 3h10l8-6M18 40v14h6v-12"/></g></svg><p>Real estate<br>investment strategies</p></div>
    <div class="topic"><svg width="72" height="72" viewBox="0 0 72 72"><circle cx="36" cy="36" r="35" fill="none" stroke="#0e426d" stroke-width="1.5"/><circle cx="36" cy="36" r="32" fill="#0e426d"/><g fill="none" stroke="#fff" stroke-width="1.6"><circle cx="30" cy="32" r="9" stroke-dasharray="4 2"/><circle cx="38" cy="38" r="7"/><path d="M43 43l9 9M20 22a20 20 0 0 1 30 0"/></g></svg><p>Due diligence</p></div>
    <div class="topic"><svg width="72" height="72" viewBox="0 0 72 72"><circle cx="36" cy="36" r="35" fill="none" stroke="#0e426d" stroke-width="1.5"/><circle cx="36" cy="36" r="32" fill="#0e426d"/><g fill="none" stroke="#fff" stroke-width="1.6"><path d="M26 24h10l-3 5c8 4 10 20-2 22h-6c-12-2-10-18-2-22z"/><ellipse cx="48" cy="32" rx="8" ry="3"/><path d="M40 32v14c0 4 16 4 16 0V32M40 37c0 4 16 4 16 0M40 42c0 4 16 4 16 0"/><circle cx="36" cy="46" r="7"/><path d="M36 42v8"/></g></svg><p>Financing</p></div>
    <div class="topic"><svg width="72" height="72" viewBox="0 0 72 72"><circle cx="36" cy="36" r="35" fill="none" stroke="#0e426d" stroke-width="1.5"/><circle cx="36" cy="36" r="32" fill="#0e426d"/><g fill="none" stroke="#fff" stroke-width="1.6"><rect x="23" y="16" width="26" height="38" rx="1"/><circle cx="36" cy="26" r="4"/><path d="M33 29l-2 6 5-2 5 2-2-6M28 40h16M28 44h16M28 48h16"/></g></svg><p>Underwriting</p></div>
    <div class="topic"><svg width="72" height="72" viewBox="0 0 72 72"><circle cx="36" cy="36" r="35" fill="none" stroke="#0e426d" stroke-width="1.5"/><circle cx="36" cy="36" r="32" fill="#0e426d"/><g fill="none" stroke="#fff" stroke-width="1.6"><path d="M32 30l6-6 6 6v8H32zM46 18h8v20h-8M20 26h8v10h-8"/><path d="M18 42h6v12h-6zM24 46h10l8-4c4-2 8 2 4 4l-12 8h-10"/></g></svg><p>Property<br>management</p></div>
    <div class="topic"><svg width="72" height="72" viewBox="0 0 72 72"><circle cx="36" cy="36" r="35" fill="none" stroke="#0e426d" stroke-width="1.5"/><circle cx="36" cy="36" r="32" fill="#0e426d"/><g fill="none" stroke="#fff" stroke-width="1.6"><rect x="20" y="16" width="26" height="38"/><rect x="24" y="20" width="26" height="38" fill="#0e426d"/><path d="M28 28h18M28 33h18M28 38h18M28 43h18M28 48h14M52 30l4 20"/></g></svg><p>Real estate<br>Legal basics</p></div>
    <div class="topic"><svg width="72" height="72" viewBox="0 0 72 72"><circle cx="36" cy="36" r="35" fill="none" stroke="#0e426d" stroke-width="1.5"/><circle cx="36" cy="36" r="32" fill="#0e426d"/><g fill="none" stroke="#fff" stroke-width="1.6"><path d="M22 18h22v14M22 18v36h16"/><path d="M26 30h12M26 36h10M26 42h8"/><circle cx="46" cy="44" r="10"/><path d="M40 44l4-3 4 3 4-2M41 47l4 2 5-3"/></g></svg><p>Sourcing deals</p></div>
    <div class="topic"><svg width="72" height="72" viewBox="0 0 72 72"><circle cx="36" cy="36" r="35" fill="none" stroke="#0e426d" stroke-width="1.5"/><circle cx="36" cy="36" r="32" fill="#0e426d"/><g fill="none" stroke="#fff" stroke-width="1.6"><rect x="31" y="29" width="10" height="14"/><path d="M33 33h6M33 37h6M36 24v-6M36 48v6M26 36h-6M46 36h6M28 28l-4-4M44 28l4-4M28 44l-4 4M44 44l4 4"/></g></svg><p>Syndication</p></div>
    <div class="topic"><svg width="72" height="72" viewBox="0 0 72 72"><circle cx="36" cy="36" r="35" fill="none" stroke="#0e426d" stroke-width="1.5"/><circle cx="36" cy="36" r="32" fill="#0e426d"/><g fill="none" stroke="#fff" stroke-width="1.6"><circle cx="28" cy="22" r="3"/><circle cx="36" cy="20" r="3"/><circle cx="44" cy="22" r="3"/><path d="M18 40l8-8h8l4 3 4-3h8l8 8M26 40l8 8 4-2 4 2 6-6"/></g></svg><p>Dealing<br>with brokers</p></div>
    <div class="topic"><svg width="72" height="72" viewBox="0 0 72 72"><circle cx="36" cy="36" r="35" fill="none" stroke="#0e426d" stroke-width="1.5"/><circle cx="36" cy="36" r="32" fill="#0e426d"/><g fill="none" stroke="#fff" stroke-width="1.6"><circle cx="42" cy="28" r="10"/><path d="M38 33l8-10"/><circle cx="39" cy="25" r="1.5"/><circle cx="45" cy="31" r="1.5"/><ellipse cx="28" cy="42" rx="7" ry="2.5"/><path d="M21 42v10c0 3 14 3 14 0V42M21 47c0 3 14 3 14 0"/></g></svg><p>Tax fundamentals</p></div>
  </div>
  <div class="footer"></div>
</div>
</body>
</html>
```